Graphic Design of Business Process

We require an eye-catching, sophisticated design of 2 business processes (attached), that will be used digitally AND for print (to be put on walls in our office).

The basic layout is attached. We require a creative, professional designer to re-design these so that they look appealing but still able to grasp all the information.

We will require vector files and editable project files for final delivery. You may refer to our website (kitefieldmedia.com.au) for an indication of our brand.

If you have any questions, please ask.

Thank you.

```html
<!DOCTYPE html>
<html lang="en">
<head>
<meta charset="utf-8">
<title>Sales and Content Funnel</title>
<link rel="stylesheet" href="https://fonts.googleapis.com/css2?family=Archivo+Black&family=Archivo:wght@500;700;800&display=swap">
<style>
  :root {
    --red: #e84c3d;
    --green: #4a9a4b;
    --orange: #f28a30;
    --blue: #2f9fd8;
    --blue-box: #2282c4;
    --title: #1a6fb0;
    --white: #ffffff;
  }
  html, body { margin: 0; padding: 0; overflow: hidden; background: var(--white); }
  .canvas { width: 1200px; height: 1200px; display: block; }
  .heading { font-family: "Archivo", Arial, sans-serif; font-weight: 800; fill: var(--title); text-anchor: middle; font-size: 40px; }
  .stage-title { font-family: "Archivo Black", Arial, sans-serif; fill: var(--white); font-size: 29px; }
  .stage-tag { font-family: "Archivo", Arial, sans-serif; font-weight: 700; font-size: 16px; }
  .bullet { font-family: "Archivo", Arial, sans-serif; font-weight: 500; fill: var(--white); font-size: 13px; }
  .funnel-title { font-family: "Archivo Black", Arial, sans-serif; fill: var(--white); text-anchor: middle; font-size: 27px; }
  .funnel-sub { font-family: "Archivo", Arial, sans-serif; font-weight: 500; fill: var(--white); font-size: 14px; text-anchor: middle; }
  .tier-title { font-family: "Archivo", Arial, sans-serif; font-weight: 800; fill: var(--white); text-anchor: middle; font-size: 52px; }
  .tier-sub { font-family: "Archivo", Arial, sans-serif; font-weight: 500; fill: var(--white); text-anchor: middle; font-size: 19px; }
  .connector { fill: none; stroke-width: 7; }
</style>
</head>
<body>
<svg class="canvas" viewBox="0 0 1500 1500" xmlns="http://www.w3.org/2000/svg">

  <g class="section-heading">
    <text class="heading" x="753" y="78">SALES &gt; CONTENT FUNNEL</text>
    <rect x="487" y="81" width="532" height="2.5" fill="var(--title)"/>
  </g>

  <g class="stage stage-awareness">
    <path d="M93,166 H372 L435,290 H93 Z" fill="var(--red)"/>
    <text class="stage-title" x="108" y="206">AWARENESS</text>
    <rect x="107" y="213" width="227" height="21" fill="var(--white)"/>
    <text class="stage-tag" x="113" y="229" fill="var(--red)">IDENTIFY PROBLEM/NEED</text>
    <circle cx="114" cy="247" r="4" fill="var(--white)"/>
    <text class="bullet" x="123" y="252">ASPIRATIONAL</text>
    <circle cx="114" cy="264" r="4" fill="var(--white)"/>
    <text class="bullet" x="123" y="269">MARKET THE OUTCOME NOT PRODUCT</text>
  </g>

  <g class="stage stage-consideration">
    <path d="M133,311 H452 L512,433 H133 Z" fill="var(--green)"/>
    <text class="stage-title" x="148" y="346">CONSIDERATION</text>
    <rect x="149" y="352" width="231" height="21" fill="var(--white)"/>
    <text class="stage-tag" x="154" y="368" fill="var(--green)">EVALUATE ALTERNATIVES</text>
    <circle cx="155" cy="384" r="4" fill="var(--white)"/>
    <text class="bullet" x="165" y="389">WHY IS THIS SOLUTION BETTER THAN OTHERS</text>
    <circle cx="155" cy="402" r="4" fill="var(--white)"/>
    <text class="bullet" x="165" y="408">HOW LONG IS THIS PROVIDER GOING TO</text>
    <text class="bullet" x="165" y="423">SOLVE MY NEED</text>
  </g>

  <g class="stage stage-action">
    <path d="M187,450 H530 L592,572 H187 Z" fill="var(--orange)"/>
    <text class="stage-title" x="207" y="496">ACTION/DECISION</text>
    <rect x="206" y="505" width="184" height="21" fill="var(--white)"/>
    <text class="stage-tag" x="212" y="521" fill="var(--orange)">PRESENT AN OFFER</text>
    <circle cx="211" cy="541" r="4" fill="var(--white)"/>
    <text class="bullet" x="220" y="546">WHICH PROVIDER?</text>
  </g>

  <g class="funnel">
    <path d="M372,165 H978 L915,300 H435 Z" fill="var(--red)"/>
    <text class="funnel-title" x="680" y="240">PROBLEM &amp; SOLUTION</text>
    <text class="funnel-sub" x="680" y="261">SUBJECTS SHOWING SYMPTOMS</text>
    <text class="funnel-sub" x="680" y="278">OF PROBLEM</text>

    <path d="M452,310 H900 L835,440 H515 Z" fill="var(--green)"/>
    <text class="funnel-title" x="680" y="367">PROVIDERS &amp; TYPES</text>
    <text class="funnel-title" x="680" y="396">OF SOLUTION</text>
    <text class="funnel-sub" x="680" y="420">SUBJECT GIVES NAME</text>
    <text class="funnel-sub" x="680" y="437">TO PROBLEM</text>

    <path d="M530,450 H820 L758,580 H595 Z" fill="var(--orange)"/>
    <text class="funnel-title" x="680" y="518">CONVERT &amp;</text>
    <text class="funnel-title" x="678" y="547">RETAIN</text>

    <path d="M612,590 H740 L677,712 Z" fill="var(--blue)"/>
  </g>

  <g class="referral-loop">
    <path class="connector" d="M1265,320 V235 H1010" stroke="var(--red)"/>
    <path d="M945,237 L1010,218 V256 Z" fill="var(--red)"/>
    <circle cx="1119" cy="240" r="40" fill="var(--red)"/>

    <path class="connector" d="M1165,378 H930" stroke="var(--green)"/>
    <path d="M868,378 L932,358 V398 Z" fill="var(--green)"/>
    <circle cx="1029" cy="378" r="40" fill="var(--green)"/>

    <path class="connector" d="M1265,437 V520 H850" stroke="var(--orange)"/>
    <path d="M790,520 L852,501 V539 Z" fill="var(--orange)"/>
    <circle cx="956" cy="520" r="40" fill="var(--orange)"/>

    <rect x="1165" y="320" width="197" height="117" fill="var(--blue-box)"/>
    <text class="funnel-title" x="1264" y="371" font-size="29">WOM &amp;</text>
    <text class="funnel-title" x="1264" y="402" font-size="29">REFERRAL</text>
  </g>

  <g class="section-heading">
    <text class="heading" x="733" y="858">CONTENT HIERARCHY</text>
    <rect x="517" y="861" width="432" height="2.5" fill="var(--title)"/>
  </g>

  <g class="pyramid">
    <path d="M733,900 L808,1032 H655 Z" fill="var(--blue)"/>

    <path d="M655,1032 H808 L887,1165 H580 Z" fill="var(--red)"/>
    <text class="tier-title" x="735" y="1113">HERO</text>
    <text class="tier-sub" x="735" y="1148">TENTPOLE CAMPAIGNS</text>

    <path d="M580,1165 H887 L963,1299 H500 Z" fill="var(--green)"/>
    <text class="tier-title" x="735" y="1235">HUB</text>
    <text class="tier-sub" x="735" y="1264">REGULAR “PUSH” CONTENT</text>

    <path d="M500,1299 H963 L1042,1432 H422 Z" fill="var(--orange)"/>
    <text class="tier-title" x="735" y="1374">HYGIENE</text>
    <text class="tier-sub" x="735" y="1402">ALWAYS-ON “PULL” CONTENT</text>
  </g>
</svg>
</body>
</html>
```